Beer Can Label design - HAZY NEIPA

Hazy NEIPA. (Acronym for New England India Pale Ale)
Full sleeve (473ml)
5.00" x 8.125" Inches
Write up on can reverse.
Opaque haze in appearance derived from specific oats, wheat, and water chemistry. This brew bolsters a dense and creamy head, leaving behind a soft and silky mouth-feel. Expect an intense tropical fruit centric aroma and flavour. Our timely hop additions contributes to less bitterness than typical IPA’s.
Logo is to be on front, towards bottom. Title near top.
Looking for something that stands out. Bold.
Target Market(s)
Craft beer enthusiasts
Industry/Entity Type
Beer & Brewing
Requirements
Must have
- Eye catching.

```html
<!DOCTYPE html>
<html lang="en">
<head>
<meta charset="utf-8">
<title>Hazy NEIPA – Can Label</title>
<link rel="stylesheet" href="https://fonts.googleapis.com/css2?family=Smokum&family=Saira+Semi+Condensed:wght@400;500&display=swap">
<style>
  :root {
    --label-green: #5a8a2a;
    --label-green-light: #7aa64e;
    --ink: #1c1c1c;
    --cream: #fbfaf5;
    --page: #ffffff;
  }
  * { box-sizing: border-box; margin: 0; padding: 0; }
  html, body { width: 1200px; height: 1000px; overflow: hidden; background: var(--page); }
  .canvas { position: relative; width: 1200px; height: 1000px; background: var(--page); }
  .label { position: absolute; left: 0; top: 0; width: 460px; height: 1000px; display: block; }
  .label__bg { fill: var(--label-green); }
  .label__pattern { fill: var(--label-green-light); opacity: 0.45; }
  .title {
    font-family: "Smokum", "Rye", serif; font-size: 175px;
    fill: var(--cream); stroke: var(--ink); stroke-width: 2.5px; paint-order: stroke;
  }
  .title-shadow { font-family: "Smokum", "Rye", serif; font-size: 175px; fill: var(--ink); }
  .tagline { font-family: "Smokum", "Rye", serif; font-size: 34px; fill: var(--ink); }
  .tagline-rule { stroke: var(--ink); stroke-width: 3px; }
  .subtitle { font-family: "Smokum", "Rye", serif; font-size: 80px; fill: var(--ink); }
  .hop { fill: var(--ink); }
  .description { font-family: "Saira Semi Condensed", "Arial Narrow", sans-serif; font-size: 13.5px; fill: var(--cream); }
  .brand { font-family: "Saira Semi Condensed", "Arial Narrow", sans-serif; font-weight: 500; font-size: 28px; fill: var(--ink); }
  .brand-dot { fill: var(--ink); }
  .volume { font-family: "Saira Semi Condensed", "Arial Narrow", sans-serif; font-size: 22px; fill: var(--cream); }
</style>
</head>
<body>
<main class="canvas">
  <svg class="label" viewBox="0 0 460 1000" xmlns="http://www.w3.org/2000/svg">
    <rect class="label__bg" width="460" height="1000"/>

    <g role="img" aria-label="faint hop leaf pattern in the corners">
      <rect class="label__pattern" x="-40" y="-10" width="90" height="150" rx="36"/>
      <rect class="label__pattern" x="410" y="-10" width="90" height="150" rx="36"/>
      <rect class="label__pattern" x="-40" y="800" width="90" height="190" rx="36"/>
      <rect class="label__pattern" x="410" y="800" width="90" height="190" rx="36"/>
    </g>

    <g class="title-block">
      <text class="title-shadow" x="70" y="230" textLength="330" lengthAdjust="spacingAndGlyphs">HAZY</text>
      <text class="title" x="65" y="225" textLength="330" lengthAdjust="spacingAndGlyphs">HAZY</text>
      <text class="title-shadow" x="80" y="420" textLength="315" lengthAdjust="spacingAndGlyphs">NEIPA</text>
      <text class="title" x="75" y="415" textLength="315" lengthAdjust="spacingAndGlyphs">NEIPA</text>
    </g>

    <g class="tagline-block">
      <line class="tagline-rule" x1="88" y1="450" x2="160" y2="450"/>
      <text class="tagline" x="170" y="463" textLength="120" lengthAdjust="spacingAndGlyphs">FOR THE</text>
      <line class="tagline-rule" x1="300" y1="450" x2="380" y2="450"/>
    </g>

    <g class="subtitle-block">
      <text class="subtitle" x="75" y="548" textLength="40" lengthAdjust="spacingAndGlyphs">H</text>
      <ellipse class="hop" cx="134" cy="520" rx="15" ry="30" role="img" aria-label="hop cone in place of the letter O"/>
      <text class="subtitle" x="152" y="548" textLength="240" lengthAdjust="spacingAndGlyphs">P HEADS</text>
    </g>

    <g class="description" text-anchor="middle">
      <text class="description" x="230" y="586" textLength="324" lengthAdjust="spacingAndGlyphs">Opaque haze in appearance derived from specific oats, wheat,</text>
      <text class="description" x="230" y="607" textLength="318" lengthAdjust="spacingAndGlyphs">and water chemistry. This brew bolsters a dense and creamy</text>
      <text class="description" x="230" y="628" textLength="309" lengthAdjust="spacingAndGlyphs">head, leaving behind a soft and silky mouth-feel. Expect an</text>
      <text class="description" x="230" y="649" textLength="324" lengthAdjust="spacingAndGlyphs">intense tropical fruit centric aroma and flavour. Our timely hop</text>
      <text class="description" x="230" y="670" textLength="309" lengthAdjust="spacingAndGlyphs">additions contributes to less bitterness than typical IPA’s.</text>
    </g>

    <g class="brand-block">
      <circle class="brand-dot" cx="92" cy="805" r="11"/>
      <text class="brand" x="112" y="815" textLength="270" lengthAdjust="spacingAndGlyphs">HARBOR CROWN BREW HOUSE</text>
    </g>

    <text class="volume" x="230" y="975" text-anchor="middle">473 ml</text>
  </svg>
</main>
</body>
</html>
```